Business card for Chiropractic clinics needs reworked / redesigned

The business card in attachment was designed 10 years ago. It is in need of an update.
We have 2 clinics:
VELDHOVE KLINIEK & VELDHOVE KLINIEK NOORD
Only one address needs to be on the card for doctors that only work in one clinic and two addresses need to be on the card for the doctors that work in both clinics.

Target Market(s)

patients/referrers

Industry/Entity Type

Medical

Contact Information for Business Card

Logo (in full or zoomed-in)
Clinic Name
Doctor name and title
clinic address, website, tel, email

Font styles to use
Sans Serif

Colors

Designer to choose colors to be used in the design.

Requirements
Must have
• Good contrast/readability
• We like modern minimalistic designs
• The Bcard needs to project our very high standard of proficiency/professionalism
Should not have
• Not curly
• Not to much colours

```html
<!DOCTYPE html>
<html lang="nl">
<head>
<meta charset="utf-8">
<title>Veldhove Kliniek – visitekaartje</title>
<link rel="stylesheet" href="https://fonts.googleapis.com/css2?family=Roboto+Condensed:wght@400;700&family=Roboto:wght@400&display=swap">
<style>
  :root {
    --ink-dark: #263b3b;
    --ink-muted: #5e7d7c;
    --paper: #ffffff;
    --backdrop: #e9ebea;
    --text-body: #3a4646;
  }
  * { margin: 0; padding: 0; box-sizing: border-box; }
  html, body { width: 1200px; height: 800px; overflow: hidden; }
  body {
    position: relative;
    background: var(--backdrop);
    font-family: "Roboto", Arial, sans-serif;
  }
  .card {
    position: absolute;
    top: 270px;
    width: 450px;
    height: 258px;
    overflow: hidden;
    box-shadow: 0 4px 10px rgba(0,0,0,.18);
  }
  .card--front { left: 132px; background: var(--ink-dark); }
  .card--back  { left: 619px; background: var(--paper); }

  .spine-motif {
    position: absolute;
    top: 0;
    height: 258px;
    background: linear-gradient(180deg, rgba(94,125,124,.55), rgba(94,125,124,.25));
  }
  .card--front .spine-motif { left: 44px; width: 110px; }
  .card--back .spine-motif  { left: 22px; width: 160px; z-index: 1; }

  .front-name {
    position: absolute;
    left: 133px;
    top: 40px;
    font-family: "Roboto Condensed", Arial, sans-serif;
    font-weight: 700;
    font-size: 24px;
    color: var(--paper);
    letter-spacing: .2px;
  }

  .band-top {
    position: absolute; left: 0; top: 0;
    width: 450px; height: 65px;
    background: var(--ink-dark);
  }
  .band-bottom {
    position: absolute; left: 0; bottom: 0;
    width: 450px; height: 13px;
    background: var(--ink-dark);
  }
  .doctor {
    position: absolute;
    right: 33px;
    top: 20px;
    text-align: right;
    z-index: 2;
  }
  .doctor-name {
    font-family: "Roboto Condensed", Arial, sans-serif;
    font-size: 18px;
    color: var(--paper);
    line-height: 22px;
  }
  .doctor-title {
    font-size: 11px;
    color: #a9bcbb;
    letter-spacing: .5px;
    line-height: 14px;
  }
  .clinic {
    position: absolute;
    right: 33px;
    text-align: right;
    font-size: 13px;
    line-height: 19px;
    color: var(--text-body);
    z-index: 2;
  }
  .clinic--main  { top: 74px; }
  .clinic--north { top: 164px; }
  .clinic-name {
    font-family: "Roboto Condensed", Arial, sans-serif;
    font-weight: 700;
    color: var(--ink-dark);
    font-size: 14px;
  }
  .divider {
    position: absolute;
    left: 268px;
    top: 155px;
    width: 149px;
    height: 1px;
    background: var(--ink-dark);
  }
</style>
</head>
<body>
  <section class="card card--front" aria-label="Voorzijde">
    <div class="spine-motif" role="img" aria-label="Ruggengraat- en rugcontour-motief"></div>
    <div class="front-name">VELDHOVE KLINIEK</div>
  </section>

  <section class="card card--back" aria-label="Achterzijde">
    <div class="band-top"></div>
    <div class="band-bottom"></div>
    <div class="spine-motif" role="img" aria-label="Ruggengraat- en rugcontour-motief"></div>

    <div class="doctor">
      <div class="doctor-name">Pieter VANDAMME D.C.</div>
      <div class="doctor-title">CHIROPRACTOR</div>
    </div>

    <div class="clinic clinic--main">
      <div class="clinic-name">VELDHOVE KLINIEK</div>
      <div>Lindenlaan 148</div>
      <div>09 000 41 28</div>
      <div>veldhovekliniek.be</div>
    </div>

    <div class="divider"></div>

    <div class="clinic clinic--north">
      <div class="clinic-name">VELDHOVE KLINIEK NOORD</div>
      <div>Kerkstraat 57</div>
      <div>09 000 62 95</div>
      <div>veldhovekliniek.be</div>
    </div>
  </section>
</body>
</html>
```